Need a sleek, professional business card design for a Web Development business

I need a unique business card designed for a web development company. It is also the parent company for any ventures I do, such as my ClipWave channel, startup ideas I have, etc. I am the single member of "Bright Harbor Code LLC." I will attach my basic logo here, so you will see the current color scheme and have the asset available. Thank you!

Target Market(s)

Startups, SMB's, Professionals

Industry/Entity Type

Business

Font styles to use
Other font styles liked:
• Lovello for headings is what I use, but not necessary.

Colors

Designer to choose colors to be used in the design.

Requirements
Nice to have
• Sleek is the word. Professional, modern, dark.
Should not have
• Any work from someone else's design. Lacking originality.

```html
<!DOCTYPE html>
<html lang="en">
<head>
<meta charset="utf-8">
<title>Bright Harbor Code LLC — Business Card</title>
<link href="https://fonts.googleapis.com/css2?family=Arimo:wght@400;700&display=swap" rel="stylesheet">
<style>
  :root {
    --stage: #0d0d0e;
    --card: #161617;
    --card-edge: #232325;
    --brand: #f2645a;
    --accent: #f0914a;
    --ink: #d6d6d6;
    --ink-soft: #a9a9a9;
  }
  * { box-sizing: border-box; margin: 0; padding: 0; }
  html, body {
    width: 1200px; height: 900px; overflow: hidden;
    background: var(--stage);
    font-family: "Arimo", Arial, sans-serif;
  }
  .stage {
    width: 1200px; height: 900px;
    display: flex; flex-direction: column;
    align-items: center; justify-content: center; gap: 60px;
  }
  .card {
    position: relative;
    width: 640px; height: 366px;
    background: var(--card);
    border: 1px solid var(--card-edge);
    border-radius: 4px;
    box-shadow: 0 18px 40px rgba(0,0,0,.6);
  }
  .brand {
    display: flex; align-items: center; gap: 12px;
    color: var(--brand);
    font-weight: 700; text-transform: uppercase;
    letter-spacing: 2px;
  }
  .brand-dot {
    width: 20px; height: 20px; border-radius: 50%;
    background: var(--accent);
  }
  /* back side */
  .card-back .brand {
    position: absolute; left: 110px; top: 120px;
    font-size: 26px;
  }
  .channel {
    position: absolute; left: 112px; top: 206px;
    display: flex; align-items: center; gap: 10px;
    font-size: 14px; color: var(--accent);
  }
  .channel-square { width: 16px; height: 16px; background: var(--accent); border-radius: 2px; }
  .channel-label { font-weight: 700; }
  .channel-divider { width: 1px; height: 18px; background: var(--ink-soft); }
  /* front side */
  .card-front .brand {
    position: absolute; left: 44px; top: 44px;
    font-size: 24px;
  }
  .person { position: absolute; left: 46px; top: 100px; }
  .person-name { font-size: 19px; color: var(--ink); font-weight: 700; }
  .person-role { font-size: 13px; color: var(--accent); margin-top: 4px; }
  .details {
    position: absolute; left: 200px; top: 172px;
    font-size: 16px; line-height: 1.5; color: var(--ink);
  }
  .address { margin-bottom: 6px; }
  .contact-list { list-style: none; }
  .contact-item { display: flex; align-items: center; gap: 10px; }
  .contact-icon { width: 16px; height: 16px; flex: none; }
</style>
</head>
<body>
<main class="stage">
  <section class="card card-back">
    <div class="brand"><span class="brand-dot"></span><span>Bright Harbor Code LLC</span></div>
    <div class="channel">
      <span class="channel-square"></span>
      <span class="channel-label">ClipWave</span>
      <span class="channel-divider"></span>
      <span>BrightHarborCode LLC</span>
    </div>
  </section>

  <section class="card card-front">
    <div class="brand"><span class="brand-dot"></span><span>Bright Harbor Code LLC</span></div>
    <div class="person">
      <p class="person-name">Owen Castell</p>
      <p class="person-role">Managing Director</p>
    </div>
    <div class="details">
      <p class="address">418 W. Larkspur Ave<br>Suite 920, P.O. Box 51842</p>
      <ul class="contact-list">
        <li class="contact-item">
          <svg class="contact-icon" viewBox="0 0 16 16" aria-hidden="true"><path d="M4 1.5l2.5 3-1.5 1.8c.8 1.8 2 3 3.7 3.7l1.8-1.5 3 2.5-1.5 2.5C7 13.5 2.5 9 1.5 3z" fill="var(--brand)"/></svg>
          <span>555.204.6187</span>
        </li>
        <li class="contact-item">
          <svg class="contact-icon" viewBox="0 0 16 16" aria-hidden="true"><rect x="1" y="3" width="14" height="10" rx="1" fill="var(--brand)"/><path d="M1.5 3.8L8 9l6.5-5.2" stroke="var(--card)" stroke-width="1.3" fill="none"/></svg>
          <span>castell@brightharborcode.com</span>
        </li>
        <li class="contact-item">
          <svg class="contact-icon" viewBox="0 0 16 16" aria-hidden="true"><circle cx="8" cy="8" r="6.5" fill="none" stroke="var(--accent)" stroke-width="1.5"/><path d="M1.5 8h13M8 1.5c2.5 3 2.5 10 0 13M8 1.5c-2.5 3-2.5 10 0 13" stroke="var(--accent)" stroke-width="1.1" fill="none"/></svg>
          <span>www.brightharborcode.com</span>
        </li>
      </ul>
    </div>
  </section>
</main>
</body>
</html>
```